Modern and sophisticated web design for architect/designer

Lumo Vant is a Building Design & Drafting studio based in Nedlands Western Australia, providing a high quality and complete client service from concept design through Council planning approvals and building licenses to construction drawings for kitchens and bathrooms, extensions, additions, renovations and new homes.

Lumo Vant is looking for a new qwerty design that *is different from a normal* 2/3 column website. The website design must be very arty, clean and catchy. This design needs to be very different and must not look like a downloadable template.

The design must be able to display a lot of photos for the different projects.

The design must comply with W3C standards (i.e. use of fonts) and must be delivered to us in A PSD layered format.

Here are a couple of example website designs that exemplify what I am after:
1) http://www.prtd.com.au/
2) http://www.martinholsbyarchitect.com/en/
3) http://veromiks.com/

I particularly like numbers 1 and 2. The third, Veromiks, jumps around a little between pages as it is actually several companies. I prefer the page design to remain steady if possible.

I like the very clever nature of number 1 (PRTD). It captures the interest, although slightly gimmicky, however I think it doesn't overpower. Its modern, and visual.

I like the clean elegant design of number 2 (Holsby), it simply delivers everything necessary in a clear intelligent manner, its attractive, menu is clever simple to use and attractive.

I would be very happy to have either of these websites.

here is another one:
4) http://www.tqarchitect.com.au/

Although this is similarly elegant, it appears quite dated. I don't like the thumbnails that you click on in the gallery, its quite clumsy. It looks minimalist, and IS minimalist, doesn't look like there is much option to expand other than changing the pictures.

If you look at my own website:
http://www.lumovant.com.au

I designed and built it myself without any skills or experience. I had to use a generic photo album generator which was worse than useless, the point I am trying to make is I tried to make the menu system a little unusual, I tried to keep the pages neat and tidy, and totally used the "black website" method. However I am more inclined to go with the lighter/white pages of (1) and (2) above because they tend to show photos better.

Dear Designers. 

ArtHive Administration has worked to provide a more comprehensive brief. Please review the amended description. 

Kind Regards, Wesley. 

Target Market(s)

Target market is people who are looking to renovate their home

Industry/Entity Type

Construction

Requirements
Must have
• The brief is to design a visual modern, elegant, sophisticated website for a small scale designer/photographer/architect that looks itself like it is designed. Not off the shelf, simple and dated. Basically the design itself has to exemplify me, it has to say "this guy is a designer, and he is good at it".

```html
<!DOCTYPE html>
<html lang="en">
<head>
<meta charset="utf-8">
<title>Lumo Vant — Building Design &amp; Drafting</title>
<link rel="stylesheet" href="https://fonts.googleapis.com/css2?family=Open+Sans:wght@400;600;700&display=swap">
<style>
  :root {
    --black: #000000;
    --nav-bg: rgba(12, 10, 10, 0.82);
    --white: #ffffff;
    --orange: #f39a12;
    --orange-text: #f5a623;
    --hero-dark: #2a1f1b;
    --hero-mid: #6b4a3a;
    --hero-warm: #8a4a2e;
    --hero-light: #b9a58e;
  }
  * { margin: 0; padding: 0; box-sizing: border-box; }
  html, body { width: 1200px; height: 687px; overflow: hidden; background: var(--black); }
  body { font-family: "Open Sans", Arial, sans-serif; color: var(--white); position: relative; }

  .hero {
    position: absolute; left: 0; top: 0; width: 1200px; height: 538px;
    background:
      radial-gradient(ellipse 420px 260px at 260px 300px, rgba(160, 80, 50, 0.75), transparent 70%),
      radial-gradient(ellipse 300px 200px at 980px 420px, rgba(215, 200, 180, 0.55), transparent 70%),
      radial-gradient(ellipse 260px 200px at 760px 280px, rgba(120, 110, 95, 0.5), transparent 70%),
      linear-gradient(180deg, var(--hero-mid) 0%, var(--hero-dark) 45%, var(--hero-warm) 75%, var(--hero-dark) 100%);
  }

  .site-nav {
    position: absolute; left: 221px; top: 0; width: 753px; height: 68px;
    background: var(--nav-bg);
  }
  .brand {
    position: absolute; left: 42px; top: 0; height: 68px;
    display: flex; align-items: center; gap: 10px;
    font-size: 15px; font-weight: 600; letter-spacing: 0.12em; text-transform: uppercase; color: var(--white);
  }
  .brand-mark { width: 12px; height: 12px; background: var(--white); }
  .nav-links { list-style: none; }
  .nav-links li { position: absolute; top: 24px; font-size: 13px; font-weight: 400; text-transform: uppercase; }
  .nav-links .active { color: var(--orange-text); }

  .hero-copy { position: absolute; right: 226px; top: 246px; text-align: right; }
  .hero-title { font-size: 46px; font-weight: 700; line-height: 56px; letter-spacing: -0.5px; }
  .hero-sub { font-size: 20px; font-weight: 400; line-height: 26px; }
  .hero-cta {
    position: absolute; right: 226px; top: 337px; width: 106px; height: 25px;
    background: rgba(18, 14, 12, 0.9); color: var(--orange-text);
    font-size: 11px; line-height: 25px; text-align: center;
  }

  .site-footer { position: absolute; left: 0; top: 538px; width: 1200px; height: 149px; background: var(--black); }
  .contact-item { position: absolute; top: 34px; display: flex; align-items: flex-start; gap: 14px; }
  .contact-icon { width: 42px; height: 42px; flex: none; }
  .contact-label { font-size: 13px; font-weight: 700; line-height: 18px; padding-top: 2px; }
  .contact-value { font-size: 13px; font-weight: 400; line-height: 18px; }
  .contact-value strong { font-weight: 700; }
  .social-dots { display: flex; gap: 7px; padding-top: 6px; }
  .social-dots span { width: 10px; height: 10px; border-radius: 50%; background: var(--white); }
</style>
</head>
<body>
  <section class="hero" role="img" aria-label="Photograph of a modern kitchen with warm granite splashback, stainless range hood, timber floor and white stone benchtop"></section>

  <nav class="site-nav">
    <div class="brand"><span class="brand-mark"></span>Lumo Vant</div>
    <ul class="nav-links">
      <li class="active" style="left:342px">Home</li>
      <li style="left:448px">About Us</li>
      <li style="left:564px">Services</li>
      <li style="left:677px">Contact</li>
    </ul>
  </nav>

  <div class="hero-copy">
    <h1 class="hero-title">Lorem ipsum</h1>
    <p class="hero-sub">dolor sit amet, consectetuer adipiscing elit</p>
  </div>
  <a class="hero-cta">Find out more &gt;</a>

  <footer class="site-footer">
    <div class="contact-item" style="left:218px">
      <svg class="contact-icon" viewBox="0 0 42 42" aria-hidden="true">
        <circle cx="21" cy="21" r="21" fill="var(--orange)"/>
        <rect x="15" y="10" width="12" height="22" rx="2" fill="none" stroke="#fff" stroke-width="2"/>
        <rect x="17.5" y="13" width="7" height="8" fill="#fff"/>
        <circle cx="21" cy="27" r="1.5" fill="#fff"/>
      </svg>
      <div>
        <div class="contact-label">Call</div>
        <div class="contact-value"><strong>T :</strong> 123 456 789</div>
      </div>
    </div>

    <div class="contact-item" style="left:524px">
      <svg class="contact-icon" viewBox="0 0 42 42" aria-hidden="true">
        <circle cx="21" cy="21" r="21" fill="var(--orange)"/>
        <rect x="11" y="14" width="20" height="14" fill="none" stroke="#fff" stroke-width="2"/>
        <path d="M11 14 L21 22 L31 14" fill="none" stroke="#fff" stroke-width="2"/>
      </svg>
      <div>
        <div class="contact-label">Contact</div>
        <div class="contact-value">info@mysite.com</div>
      </div>
    </div>

    <div class="contact-item" style="left:834px">
      <svg class="contact-icon" viewBox="0 0 42 42" aria-hidden="true">
        <circle cx="21" cy="21" r="21" fill="var(--orange)"/>
        <circle cx="21" cy="21" r="12" fill="none" stroke="#fff" stroke-width="2.5"/>
        <path d="M21 14 V28 M14 21 H28" stroke="#fff" stroke-width="3"/>
      </svg>
      <div>
        <div class="contact-label">Follow</div>
        <div class="social-dots"><span></span><span></span><span></span><span></span></div>
      </div>
    </div>
  </footer>
</body>
</html>
```